Website for our 3rd party logistics warehouse company

Our company is a 3rd party logistics company. We receive and ship other businesses products for them. We offer our services to other smaller businesses that do not have a warehouse to operate out of. We also help many Brindlemart businesses prepare their products to be sold on Brindlemart.

We are looking for a modern looking design for our website. Please see our attached logo for design ideas. We are open to changing logo colors for website.

We really like the look of the website www.quorvane.com

Target Market(s)

Other businesses and brands of products

Industry/Entity Type

Warehousing and shipping

Number of Pages Required

2 page

Requirements
Must have
• We need 2 pages. Our main landing page and a duplicate page with different information geared towards brands.
Nice to have
• I like the look of overlay/transparent sections. Please see quorvane.com there is a ribbon that shows "Partners".

```html
<!DOCTYPE html>
<html lang="en">
<head>
<meta charset="utf-8">
<title>Orbitline 3PL — Logistics Solutions</title>
<link href="https://fonts.googleapis.com/css2?family=Bebas+Neue&family=Rubik:wght@300;400;500;600&display=swap" rel="stylesheet">
<style>
:root{
  --yellow:#fdc82f;
  --yellow-pale:#fdeeb8;
  --ink:#222630;
  --text:#5d6370;
  --muted:#9aa0ab;
  --line:#e6e7ea;
  --light-bg:#f6f6f7;
  --footer:#1f1f22;
  --footer-deep:#19191b;
  --white:#ffffff;
}
*{box-sizing:border-box;margin:0;padding:0}
html,body{width:1200px;height:3698px;overflow:hidden}
body{font-family:"Rubik",Arial,sans-serif;color:var(--ink);background:var(--white);position:relative}
section,header,footer{position:absolute;left:0;width:1200px}
.abs{position:absolute}
.btn{position:absolute;display:flex;align-items:center;justify-content:center;gap:10px;background:var(--yellow);color:var(--ink);border-radius:30px;font-weight:500;font-size:12px;text-transform:uppercase;letter-spacing:.2px}
.mark{position:absolute;width:26px;height:4px;border-radius:2px;background:var(--yellow)}
.sec-title{position:absolute;font-size:22px;font-weight:500;text-transform:uppercase;color:var(--ink)}

/* hero */
.hero{top:0;height:669px;background:linear-gradient(155deg,#2b3a4c 0%,#1d2838 35%,#3a3f3a 60%,#6b5a2c 100%);overflow:hidden}
.hero-photo{position:absolute;inset:0;background:
  radial-gradient(ellipse at 80% 30%,rgba(120,140,170,.45),transparent 55%),
  radial-gradient(ellipse at 70% 75%,rgba(214,164,56,.45),transparent 50%),
  linear-gradient(180deg,rgba(10,16,26,.35),rgba(10,16,26,.55))}
.logo{position:absolute;color:var(--white);font-weight:500;font-size:17px;letter-spacing:1.5px;display:flex;align-items:center;gap:8px}
.logo .dot{width:10px;height:10px;border-radius:50%;background:var(--yellow)}
.nav{position:absolute;left:481px;top:50px;display:flex;gap:17px;color:var(--white);font-size:12.5px;font-weight:500}
.phone{position:absolute;left:874px;top:34px;width:168px;height:41px;background:var(--yellow);border-radius:21px;display:flex;align-items:center;justify-content:center;gap:10px;font-weight:500;font-size:14.5px;color:var(--ink)}
.eyebrow{position:absolute;left:155px;top:228px;color:var(--yellow);font-size:16px;font-weight:500}
.hero-title{position:absolute;left:155px;top:262px;color:var(--white);font-family:"Bebas Neue",Impact,sans-serif;font-size:60px;line-height:58px;letter-spacing:1px;font-weight:400}
.slider-dots{position:absolute;left:1070px;top:274px}
.slider-dots span{position:absolute;left:0;width:6px;height:6px;border-radius:50%;background:var(--white)}
.partners{position:absolute;left:0;top:590px;width:1200px;height:79px;background:rgba(15,20,30,.55);display:flex;padding-left:155px}
.partner{height:79px;display:flex;align-items:center;color:rgba(255,255,255,.8);font-weight:500;font-size:16px;gap:10px;border-right:1px solid rgba(255,255,255,.12)}
.partner .sq{width:22px;height:22px;border:2px solid rgba(255,255,255,.75)}
.partner:last-child{border-right:none}

/* who */
.who{top:669px;height:468px}
.photo-card{position:absolute;display:flex;align-items:flex-end;padding:0 0 16px 18px;color:var(--white);font-size:12.5px;font-weight:600}
.dots-grid{position:absolute;background-image:radial-gradient(circle,#b5bac3 1.2px,transparent 1.6px);background-size:16px 16px}
.who h2{position:absolute;left:696px;top:156px;font-size:22px;font-weight:500}
.who .sub{position:absolute;left:699px;top:198px;font-size:13px;font-weight:500;color:var(--ink)}
.who p{position:absolute;left:699px;top:228px;width:350px;font-size:12.5px;line-height:24px;color:var(--text);font-weight:300}

/* why */
.why{top:1137px;height:406px;background:var(--light-bg)}
.card{position:absolute;top:127px;width:203px;height:226px;background:var(--white);border:1px solid var(--line);text-align:center;overflow:hidden}
.card .icon{width:58px;height:58px;margin:26px auto 0;border-radius:50%;background:var(--yellow-pale)}
.card p{margin:14px 18px 0;font-size:12.5px;line-height:22.5px;color:var(--text);font-weight:300}
.card .wave{position:absolute;left:0;bottom:6px}

/* benefits */
.benefits{top:1543px;height:403px;background:linear-gradient(180deg,#1a2232 0%,#121a28 45%,#2c2a22 100%);overflow:hidden}
.benefits .glow{position:absolute;inset:0;background:radial-gradient(ellipse at 50% 100%,rgba(200,160,50,.28),transparent 60%)}
.benefits h2{position:absolute;left:0;width:1200px;top:78px;text-align:center;color:var(--yellow);font-size:22px;font-weight:500}
.benefit{position:absolute;top:186px;color:var(--white);font-size:12.5px;line-height:24px}
.benefit .icon{width:56px;height:56px;border-radius:8px;background:var(--yellow);margin-bottom:10px}
.vline{position:absolute;top:170px;width:1px;height:170px;background:rgba(255,255,255,.12)}

/* software */
.software{top:1946px;height:416px}
.software p{position:absolute;left:158px;top:154px;width:330px;font-size:12.5px;line-height:24px;color:var(--text)}
.dash-panel{position:absolute;left:537px;top:74px;width:238px;height:276px;background:linear-gradient(180deg,#ffffff,#f3f4f8);box-shadow:0 6px 24px rgba(30,40,60,.1)}
.tablet{position:absolute;left:790px;top:62px;width:270px;height:210px;border-radius:16px;background:linear-gradient(135deg,#c7b4b8,#e9eef6 55%,#f5f7fb);transform:rotate(24deg);box-shadow:0 14px 30px rgba(30,40,60,.18);border:6px solid #f3f4f7}

/* guarantee */
.guarantee{top:2362px;height:454px;background:var(--light-bg)}
.team-photo{position:absolute;left:0;top:0;width:624px;height:454px;background:linear-gradient(160deg,#6f7378 0%,#9aa29a 40%,#4d5446 70%,#2b3140 100%)}
.guarantee p{position:absolute;left:692px;top:277px;width:330px;font-size:12.5px;line-height:24px;color:var(--text)}
.g-icon{position:absolute;top:152px;width:56px;height:56px;border-radius:50%;background:var(--yellow)}
.g-label{position:absolute;top:230px;font-size:12.5px;color:var(--text)}

/* contact */
.contact{top:2816px;height:516px}
.field{position:absolute;border:1px solid var(--line);display:flex;align-items:center;justify-content:space-between;padding:0 20px 0 23px;font-size:12.5px;color:var(--muted)}

/* footer */
.footer{top:3332px;height:366px;background:var(--footer)}
.footer h4{position:absolute;top:72px;color:var(--white);font-size:14.5px;font-weight:500}
.footer .info{position:absolute;top:108px;color:#d6d7da;font-size:13px;line-height:30px}
.social{position:absolute;left:839px;top:115px;display:flex;gap:16px;color:#d6d7da;font-size:12px}
.footer-bottom{position:absolute;left:0;top:198px;width:1200px;height:168px;background:var(--footer-deep)}
.fine{position:absolute;left:155px;top:32px;width:880px;font-size:8.5px;line-height:15px;color:#6d6f74}
.copy{position:absolute;left:0;width:1200px;top:114px;text-align:center;font-size:9px;color:#6d6f74}
</style>
</head>
<body>

<header class="hero">
  <div class="hero-photo" role="img" aria-label="Aerial night photo of a busy warehouse yard with trucks at loading docks"></div>
  <div class="logo" style="left:158px;top:46px"><span class="dot"></span>ORBITLINE 3PL</div>
  <nav class="nav"><span>HOME</span><span>GROW</span><span>DISTRIBUTE</span><span>ABOUT US</span><span>CONTACT US</span></nav>
  <div class="phone">
    <svg width="16" height="16" viewBox="0 0 24 24" fill="none" stroke="#222630" stroke-width="2"><path d="M22 16.9v3a2 2 0 0 1-2.2 2 19.8 19.8 0 0 1-8.6-3.1 19.5 19.5 0 0 1-6-6A19.8 19.8 0 0 1 2.1 4.2 2 2 0 0 1 4.1 2h3a2 2 0 0 1 2 1.7c.1 1 .4 1.9.7 2.8a2 2 0 0 1-.5 2.1L8 9.9a16 16 0 0 0 6 6l1.3-1.3a2 2 0 0 1 2.1-.4c.9.3 1.8.6 2.8.7a2 2 0 0 1 1.7 2z"/></svg>
    (555) 204 71 38
  </div>
  <div class="eyebrow">SIMPLE AND SMART WAREHOUSING</div>
  <h1 class="hero-title">LOGISTICS SOLUTIONS<br>AROUND THE WORLD</h1>
  <div class="btn" style="left:155px;top:400px;width:171px;height:45px">CONTACT US NOW</div>
  <div class="slider-dots">
    <span style="top:3px"></span>
    <span style="top:33px;width:14px;height:14px;left:-4px;border:2px solid rgba(253,200,47,.5);background:var(--yellow);background-clip:content-box;padding:2px"></span>
    <span style="top:67px"></span>
  </div>
  <div class="partners">
    <div class="partner" style="width:158px"><span class="sq"></span>NORTHVALE</div>
    <div class="partner" style="width:182px;padding-left:26px">KESTROW</div>
    <div class="partner" style="width:208px;padding-left:26px">PLENWICK.CO</div>
    <div class="partner" style="width:184px;padding-left:30px">Torvana</div>
    <div class="partner" style="width:200px;padding-left:40px;letter-spacing:2px">MERIDOX</div>
  </div>
</header>

<section class="who">
  <div class="dots-grid" style="left:140px;top:54px;width:100px;height:8px"></div>
  <div class="dots-grid" style="left:140px;top:54px;width:8px;height:100px"></div>
  <div class="photo-card" style="left:156px;top:70px;width:240px;height:297px;background:linear-gradient(170deg,#7a5a4a 0%,#d48c4a 35%,#3b4a5e 70%,#1e2632 100%)" role="img" aria-label="Cargo plane over shipping containers and a truck at sunset">LOGISTICS &nbsp;<span style="color:var(--yellow)">↗</span></div>
  <div class="photo-card" style="left:419px;top:102px;width:225px;height:297px;background:linear-gradient(180deg,#4d5a70 0%,#7d6a58 50%,#3a3f4a 100%)" role="img" aria-label="Warehouse interior with stacked pallets and racks">WAREHOUSE &nbsp;<span style="color:var(--yellow)">↗</span></div>
  <div class="dots-grid" style="left:574px;top:410px;width:90px;height:8px"></div>
  <div class="dots-grid" style="left:656px;top:330px;width:8px;height:88px"></div>
  <div class="mark" style="left:697px;top:136px"></div>
  <h2>WHO WE ARE</h2>
  <div class="sub">Your Logistics Warehouse Solutions Provider</div>
  <p>Orbitline 3PL is your one stop 3PL that will help you grow your business and allow you to be hands off. We offer high end services and meet our commitment, guaranteed.</p>
  <div class="btn" style="left:695px;top:320px;width:133px;height:40px;font-size:11px">MORE DETAILS</div>
</section>

<section class="why">
  <div class="mark" style="left:588px;top:49px"></div>
  <h2 class="sec-title" style="left:0;width:1200px;text-align:center;top:72px">WHY USE A ORBITLINE 3PL?</h2>

  <div class="card" style="left:155px">
    <div class="icon" role="img" aria-label="Icon of a globe with a location pin"></div>
    <p>Work from anywhere<br>in the world.</p>
    <svg class="wave" width="203" height="16" viewBox="0 0 203 16"><path d="M0 10c40 0 60-8 100-8s60 8 103 6" fill="none" stroke="#fdc82f" stroke-width="1.5"/></svg>
  </div>
  <div class="card" style="left:384px">
    <div class="icon" role="img" aria-label="Icon of a worker with a thought bubble"></div>
    <p>Don't have to manage employees, health insurance plans, payroll, sick calls, etc.</p>
    <svg class="wave" width="203" height="16" viewBox="0 0 203 16"><path d="M0 10c40 0 60-8 100-8s60 8 103 6" fill="none" stroke="#fdc82f" stroke-width="1.5"/></svg>
  </div>
  <div class="card" style="left:611px">
    <div class="icon" role="img" aria-label="Icon of a warehouse with boxes"></div>
    <p>Don't get locked into a 3-5 year warehouse lease where you guarantee hundreds of thousands of dollars</p>
    <svg class="wave" width="203" height="16" viewBox="0 0 203 16"><path d="M0 10c40 0 60-8 100-8s60 8 103 6" fill="none" stroke="#fdc82f" stroke-width="1.5"/></svg>
  </div>
  <div class="card" style="left:839px">
    <div class="icon" role="img" aria-label="Icon of growth arrows above a thumbs up"></div>
    <p>Grow your business<br>without commitment</p>
    <svg class="wave" width="203" height="16" viewBox="0 0 203 16"><path d="M0 10c40 0 60-8 100-8s60 8 103 6" fill="none" stroke="#fdc82f" stroke-width="1.5"/></svg>
  </div>
</section>

<section class="benefits" role="img" aria-label="Dusk photo of a large distribution center with lit loading docks">
  <div class="glow"></div>
  <div class="mark" style="left:588px;top:56px"></div>
  <h2>ORBITLINE 3PL BENEFITS</h2>

  <div class="benefit" style="left:156px"><div class="icon"></div>48 hour turn around<br>guarantee – done in<br>48 hours or its free*</div>
  <div class="vline" style="left:320px"></div>
  <div class="benefit" style="left:357px"><div class="icon"></div>No monthly<br>subscription – only<br>pay for what you use</div>
  <div class="vline" style="left:519px"></div>
  <div class="benefit" style="left:560px"><div class="icon"></div>No receiving fees</div>
  <div class="vline" style="left:696px"></div>
  <div class="benefit" style="left:749px"><div class="icon"></div>No pallet or<br>outbound fees</div>
  <div class="vline" style="left:864px"></div>
  <div class="benefit" style="left:931px"><div class="icon"></div>Email and<br>phone support</div>
</section>

<section class="software">
  <div class="mark" style="left:160px;top:80px"></div>
  <h2 class="sec-title" style="left:158px;top:110px">OUR SOFTWARE</h2>
  <p>Know what inventory is at our warehouse in real time. Our software allows you to track your inventory and know how your shipment status in real time. Professional software designed specifically for our needs.</p>
  <div class="btn" style="left:155px;top:265px;width:133px;height:38px;font-size:11px">MORE DETAILS</div>

  <div class="tablet" role="img" aria-label="Tablet showing an analytics dashboard"></div>
  <div class="dash-panel" role="img" aria-label="Dashboard card with a sales bar chart"></div>
</section>

<section class="guarantee">
  <div class="team-photo" role="img" aria-label="Team of warehouse staff in safety vests standing between storage racks"></div>
  <div class="mark" style="left:694px;top:58px"></div>
  <h2 class="sec-title" style="left:690px;top:88px">OUR GUARANTEE</h2>
  <div class="g-icon" style="left:704px" role="img" aria-label="Fast 48 hour badge icon"></div>
  <div class="g-icon" style="left:818px" role="img" aria-label="Hand with discount badge icon"></div>
  <div class="g-label" style="left:692px">Business Hours</div>
  <div class="g-label" style="left:816px">We offer a 500 item (up to $700)</div>
  <p>All orders will be prepped and ready for shipment in 48 business hours (often 24 or less) and we guarantee it. We are confident in our services and if we do not fulfill our obligation, we offer a 500 item (up to $700) credit on your next shipment.</p>
</section>

<section class="contact">
  <div class="mark" style="left:588px;top:30px"></div>
  <h2 class="sec-title" style="left:0;width:1200px;text-align:center;top:70px">TYPE US A WORD</h2>
  <div class="field" style="left:230px;top:134px;width:357px;height:58px">Full Name
    <svg width="20" height="22" viewBox="0 0 20 22" fill="none" stroke="#c3c6cc" stroke-width="1.3"><rect x="2" y="6" width="16" height="15"/><rect x="6" y="1" width="8" height="5"/><path d="M6 11h8M6 15h8"/></svg></div>
  <div class="field" style="left:620px;top:134px;width:358px;height:58px">Email Address
    <svg width="20" height="16" viewBox="0 0 20 16" fill="none" stroke="#c3c6cc" stroke-width="1.3"><rect x="1" y="2" width="18" height="12"/><path d="M1 2l9 7 9-7"/></svg></div>
  <div class="field" style="left:230px;top:216px;width:357px;height:58px">Company Name
    <svg width="20" height="22" viewBox="0 0 20 22" fill="none" stroke="#c3c6cc" stroke-width="1.3"><rect x="3" y="2" width="14" height="19"/><path d="M7 6h2M11 6h2M7 10h2M11 10h2M7 14h2M11 14h2"/></svg></div>
  <div class="field" style="left:620px;top:216px;width:358px;height:58px">Your Topic
    <svg width="20" height="22" viewBox="0 0 20 22" fill="none" stroke="#c3c6cc" stroke-width="1.3"><rect x="3" y="2" width="14" height="19"/><path d="M6 8h8M6 12h8M6 16h5"/></svg></div>
  <div class="field" style="left:231px;top:292px;width:747px;height:104px;align-items:flex-start;justify-content:flex-start;gap:14px;padding-top:26px">Message
    <svg width="24" height="18" viewBox="0 0 24 18" fill="none" stroke="#c3c6cc" stroke-width="1.3"><rect x="1" y="1" width="16" height="11" rx="1"/><path d="M7 12v4l4-4M19 5h4v10h-3v3l-3-3h-6"/></svg></div>
  <div class="btn" style="left:517px;top:424px;width:172px;height:51px;font-size:11.5px">SEND MESSAGE <span>↗</span></div>
</section>

<footer class="footer">
  <div class="logo" style="left:166px;top:92px;font-size:17px"><span class="dot"></span>ORBITLINE 3PL</div>
  <h4 style="left:387px">Contact us</h4>
  <div class="info" style="left:387px">hello@orbitline-mail.net<br>+(555)310-482-9061</div>
  <h4 style="left:611px">Visit us</h4>
  <div class="info" style="left:611px">2417 Fernhollow Road,<br>Castelby, OR 97402</div>
  <h4 style="left:839px">Follow us</h4>
  <div class="social"><span>Wavely</span><span>Chirpnet</span><span>Plusring</span></div>
  <div class="footer-bottom">
    <p class="fine">*Our guarantee is 48 hours from the time an outbound shipment is created in our system. Weekends and holidays excluded. Orders created on a Friday after hours, Saturday or Sunday will be counted from the open of business on Monday morning. We offer a credit of up to 500 units on your next shipment. These credits are for standard prep items only, not bundles, bubble wrapped or multipack units. Outbound shipments will be prepped and ready to ship. We are unable to control shipping companies and freight carriers. Orders after daily pickups are completed will be ready for next day pickup.</p>
    <div class="copy">© 2021 ORBITLINE 3PL .com. All Rights Reserved</div>
  </div>
</footer>

</body>
</html>
```